Brookvine Estates Business Card

Business Card:

Somewhere on front of card, please include Broker License Number: 5839261

Website is BrookvineEstates.com

Address is:
7216 Orchardpine Ave E
Saginaw, MI 48517

I'll let you use creative freedom on the rest; we obviously need Name, Title, Email (@BrookvineEstates.com), Office Phone, Cell Phone.

Don't want any special die-cutting, just a standard size business card.

On the back, include a place for the date and time of an appointment to be written in pen.

Industry/Entity Type

Business

Requirements
Must have
• Our logo, attached to email.

```html
<!DOCTYPE html>
<html lang="en">
<head>
<meta charset="utf-8">
<title>Brookvine Estates Business Card</title>
<link href="https://fonts.googleapis.com/css2?family=Source+Sans+3:wght@400;600&display=swap" rel="stylesheet">
<style>
  :root {
    --stage: #3b3b3b;
    --paper: #f7f7f7;
    --navy: #23236e;
    --navy-text: #24246c;
    --rule: #5a5a5a;
    --muted: #555555;
    --white: #ffffff;
  }
  * { margin: 0; padding: 0; box-sizing: border-box; }
  html, body { width: 1200px; height: 750px; overflow: hidden; }
  body {
    background: var(--stage);
    font-family: "Source Sans 3", sans-serif;
    position: relative;
  }
  .card {
    position: absolute;
    top: 228px;
    width: 462px;
    height: 262px;
    background: var(--paper);
  }
  .card-front { left: 124px; }
  .card-back { left: 618px; }

  .brand-panel {
    position: absolute; left: 0; top: 0;
    width: 242px; height: 100%;
    display: flex; align-items: center; justify-content: center;
  }
  .brand-name {
    color: var(--navy);
    font-weight: 600;
    font-size: 23px;
    letter-spacing: 0.2px;
  }
  .contact-panel {
    position: absolute; left: 244px; top: 0;
    width: 218px; height: 100%;
    background: var(--navy);
    color: var(--white);
  }
  .person-name {
    position: absolute; top: 42px; left: 20px;
    font-size: 17px; font-weight: 600;
  }
  .person-title {
    position: absolute; top: 62px; left: 20px;
    font-size: 13px;
  }
  .address {
    position: absolute; top: 97px; left: 20px;
    font-size: 11.5px; line-height: 14px;
  }
  .contact-list {
    position: absolute; top: 134px; left: 20px;
    list-style: none;
    font-size: 11.5px;
  }
  .contact-list li {
    display: flex; align-items: center;
    height: 17.6px;
    white-space: nowrap;
  }
  .contact-list svg { width: 11px; height: 11px; margin-right: 6px; fill: var(--white); flex: none; }
  .license {
    position: absolute; top: 207px; left: 20px;
    font-size: 11.5px;
  }

  .field-label {
    position: absolute;
    color: var(--navy-text);
    font-size: 14px;
    line-height: 16px;
  }
  .field-rule, .note-rule {
    position: absolute;
    height: 1px;
    background: var(--rule);
  }
  .ampm {
    position: absolute; right: 34px; top: 46px;
    font-size: 10px; line-height: 11px;
    color: var(--navy-text);
  }
  .back-url {
    position: absolute; bottom: 22px; left: 0; width: 100%;
    text-align: center;
    font-size: 11px; letter-spacing: 2.4px;
    color: var(--muted);
  }
</style>
</head>
<body>
  <section class="card card-front">
    <div class="brand-panel">
      <span class="brand-name">Brookvine Estates</span>
    </div>
    <div class="contact-panel">
      <div class="person-name">Daniel Hartley</div>
      <div class="person-title">CEO/Founder</div>
      <div class="address">7216 Orchardpine Ave E<br>Saginaw, MI 48517</div>
      <ul class="contact-list">
        <li><svg viewBox="0 0 24 24"><path d="M6.6 10.8c1.4 2.8 3.8 5.1 6.6 6.6l2.2-2.2c.3-.3.7-.4 1-.2 1.1.4 2.3.6 3.6.6.6 0 1 .4 1 1V20c0 .6-.4 1-1 1C10.6 21 3 13.4 3 4c0-.6.4-1 1-1h3.5c.6 0 1 .4 1 1 0 1.3.2 2.5.6 3.6.1.3 0 .7-.2 1z"/></svg>989 214 7730</li>
        <li><svg viewBox="0 0 24 24"><path d="M7 1h10a2 2 0 0 1 2 2v18a2 2 0 0 1-2 2H7a2 2 0 0 1-2-2V3a2 2 0 0 1 2-2zm0 3v16h10V4z"/></svg>989 556 3182</li>
        <li><svg viewBox="0 0 24 24"><path d="M2 5h20v14H2zm2 2v.5l8 5 8-5V7zm0 3v7h16v-7l-8 5z"/></svg>name@BrookvineEstates.com</li>
        <li><svg viewBox="0 0 24 24"><circle cx="12" cy="12" r="10"/></svg>www.BrookvineEstates.com</li>
      </ul>
      <div class="license">Broker Lic No: 5839261</div>
    </div>
  </section>

  <section class="card card-back">
    <span class="field-label" style="left:29px; top:41px;">Date :</span>
    <div class="field-rule" style="left:30px; top:60px; width:212px;"></div>
    <span class="field-label" style="left:256px; top:40px;">Time :</span>
    <div class="field-rule" style="left:260px; top:60px; width:168px;"></div>
    <span class="ampm">AM/PM</span>

    <div class="note-rule" style="left:32px; top:97px; width:396px;"></div>
    <div class="note-rule" style="left:32px; top:134px; width:396px;"></div>
    <div class="note-rule" style="left:32px; top:170px; width:396px;"></div>
    <div class="note-rule" style="left:32px; top:206px; width:396px;"></div>

    <div class="back-url">www.BrookvineEstates.com</div>
  </section>
</body>
</html>
```